Stylish Aluminum Fence Sales Brochure

We would like to have an Aluminum Fence Brochure that is tailored to our business name and branded to our business specifically. These are examples of aluminum fencing brochures that we would like to have:

http://dealers.brightrailco.example/Docs.nsf/2016_HarborlineBrochure_Final%204%207%2016.pdf
and
http://dealers.brightrailco.example/Docs.nsf/Harborline%20Residential.pdf

We would like this to be a front and back brochure. The front should be decorative with fence photos and our logo and information. The back should contain the different styles of aluminum fences similar to this brochure has:
http://www.tamblerailworks.example/images/flyers/2014Singles/TRWflyerRear2014.jpg

We would like the brochure to have information similar to the brightrailco brochures but be similar in design/layout to the Tamble brochure:
http://www.tamblerailworks.example/images/flyers/2014Singles/TRWflyerFront2014.jpg <-- FRONT
http://www.tamblerailworks.example/images/flyers/2014Singles/TRWflyerRear2014.jpg <-- BACK

We have attached some photos of our own fencing to be used in the photos, including some of these:
https://www.facebook.com/MapleGateFenceRLX/photos/a.111222333444555.2223334445556.666777888999000/123123123123123/?type=3&theater
https://www.facebook.com/MapleGateFenceRLX/photos/a.444555666777888.2223334445557.666777888999000/321321321321321/?type=3&theater
https://www.facebook.com/MapleGateFenceRLX/photos/a.444555666777888.2223334445557.666777888999000/456456456456456/?type=3&theater

We need someone who has a creative vision in order to create this document. This will be a sales flyer that we will use all the time.

Our business name is Maple Gate Fence. Website: http://www.mybrookvalegates.example
Our logo and business information is on the website.

Target Market(s)

Residential Customers

Industry/Entity Type

Fence

Font styles to use
Sans Serif

Colors
0455a3
0592cd
33a6d7
3176b5
85abd2
85cae6
cee9f5
f8fafc
fbf289

Requirements
Must have
• Fence photos on one side and the aluminum fence style images on the reverse side
Nice to have
• Clear images, information about the fence warranty, specs on the designs
Should not have
• Only our business name, Maple Gate Fence

```html
<!DOCTYPE html>
<html lang="en">
<head>
<meta charset="utf-8">
<title>Maple Gate Fence – Aluminum Fences</title>
<link href="https://fonts.googleapis.com/css2?family=Open+Sans:ital,wght@0,400;0,600;0,700;0,800;1,400;1,600&display=swap" rel="stylesheet">
<style>
  :root{
    --brand-orange:#e0781f;
    --ink:#2b2b2b;
    --body-text:#3c3c3c;
    --band-blue:#0592cd;
    --band-deep:#0455a3;
    --sky:#85cae6;
    --paper:#ffffff;
    --photo-green:#6f8f4a;
    --photo-sky:#a9c6dc;
    --photo-dark:#2f3a2a;
  }
  *{box-sizing:border-box;margin:0;padding:0}
  html,body{width:849px;height:1200px;overflow:hidden;background:var(--paper)}
  body{font-family:"Open Sans",Arial,sans-serif;color:var(--ink);position:relative}

  .brand-header{position:absolute;left:34px;top:26px;display:flex;align-items:flex-start;gap:14px}
  .brand-square{width:60px;height:60px;background:var(--brand-orange);margin-top:4px}
  .brand-name{font-size:34px;font-weight:700;color:var(--brand-orange);line-height:1.05}
  .brand-phone{font-size:32px;font-weight:800;color:var(--ink);line-height:1.1;letter-spacing:.5px}
  .brand-tagline{font-size:11px;font-style:italic;font-weight:600;color:var(--ink);margin-top:2px}

  .photo-collage{position:absolute;left:0;top:110px;width:849px;height:510px}

  .styles-section{position:absolute;left:0;top:620px;width:849px;text-align:center}
  .styles-title{font-size:28px;font-weight:800;letter-spacing:.5px;color:var(--ink)}
  .style-list{display:flex;justify-content:space-between;padding:0 40px;margin-top:14px;list-style:none}
  .style-item{width:180px;display:flex;flex-direction:column;align-items:center}
  .style-thumb{width:84px;height:64px;border-radius:8px;background:linear-gradient(180deg,var(--photo-sky),var(--photo-green))}
  .style-label{font-size:13px;font-weight:600;margin-top:8px;letter-spacing:.3px;text-transform:uppercase}

  .about{position:absolute;left:48px;top:790px;width:753px;font-size:14.5px;font-style:italic;line-height:1.5;color:var(--body-text)}
  .about p+p{margin-top:18px}

  .contact-band{position:absolute;left:0;top:990px;width:849px;height:210px;background:var(--band-blue);color:#fff;text-align:center;padding-top:22px}
  .contact-title{font-size:30px;font-weight:800;letter-spacing:1px}
  .contact-lines{font-size:12px;line-height:1.6;margin-top:8px}
  .contact-site{font-size:12px;margin-top:16px}
</style>
</head>
<body>

<header class="brand-header">
  <div class="brand-square"></div>
  <div>
    <div class="brand-name">Maple Gate Fence</div>
    <div class="brand-phone">555-310-4482</div>
    <div class="brand-tagline">"Because Good Fences Make Good Neighbors"</div>
  </div>
</header>

<svg class="photo-collage" viewBox="0 0 849 510" aria-hidden="false">
  <defs>
    <linearGradient id="yard" x1="0" y1="0" x2="0" y2="1">
      <stop offset="0" stop-color="#b7cfe0"/>
      <stop offset=".45" stop-color="#c9b89a"/>
      <stop offset="1" stop-color="#6f8f4a"/>
    </linearGradient>
    <linearGradient id="lawn" x1="0" y1="0" x2="0" y2="1">
      <stop offset="0" stop-color="#a9c6dc"/>
      <stop offset=".5" stop-color="#7e9c5a"/>
      <stop offset="1" stop-color="#55703a"/>
    </linearGradient>
    <linearGradient id="shade" x1="0" y1="0" x2="1" y2="1">
      <stop offset="0" stop-color="#8fae70"/>
      <stop offset="1" stop-color="#3e5530"/>
    </linearGradient>
  </defs>
  <g stroke="#ffffff" stroke-width="6">
    <polygon role="img" aria-label="Black aluminum fence running along a sloped yard" points="40,120 560,20 580,270 70,400" fill="url(#yard)"/>
    <polygon role="img" aria-label="Arched aluminum gate in a grassy yard" points="560,20 820,20 820,130 580,150" fill="url(#lawn)"/>
    <polygon role="img" aria-label="Aluminum fence around a backyard with trees" points="580,160 820,150 820,470 600,470" fill="url(#shade)"/>
    <polygon role="img" aria-label="Aluminum fence and gate beside a house" points="280,300 580,270 600,470 300,480" fill="url(#lawn)"/>
    <polygon role="img" aria-label="Aluminum fence along a lawn edge" points="30,370 290,320 300,480 30,485" fill="url(#shade)"/>
  </g>
</svg>

<section class="styles-section">
  <h2 class="styles-title">ALUMINUM FENCES</h2>
  <ul class="style-list">
    <li class="style-item"><div class="style-thumb" role="img" aria-label="Flat top fence style"></div><span class="style-label">Flat Top Fences</span></li>
    <li class="style-item"><div class="style-thumb" role="img" aria-label="Flat top with spears fence style"></div><span class="style-label">Flat Top With Spears</span></li>
    <li class="style-item"><div class="style-thumb" role="img" aria-label="Spear top fence style"></div><span class="style-label">Spear Top Fences</span></li>
    <li class="style-item"><div class="style-thumb" role="img" aria-label="Staggered spear fence style"></div><span class="style-label">Staggered Spear</span></li>
  </ul>
</section>

<section class="about">
  <p>Maple Gate Fence consists of a growing team of individuals with over 30 years of experience within the fencing industry. Each member of our staff is well-trained and knowledgeable within their own specialty. All of our installers take pride in the work completed. In our eyes, we are only as successful as the completion of your job – each job is important to us and we strive to give you the best installation experience possible.</p>
  <p>There are many benefits to contracting Maple Gate Fence for your outdoor living needs. We always provide free estimates, can assist with HOA approvals, and provide an outstanding warranty for all workmanship.</p>
</section>

<footer class="contact-band">
  <div class="contact-title">CONTACT US</div>
  <div class="contact-lines">
    Phone: 555-310-4482 &nbsp;|&nbsp; Email: office@mybrookvalegates.example<br>
    Address: 4120 Orchard Ridge Rd, Brookvale NC 28900<br>
    Office hours: Monday - Friday 9AM - 4PM Saturday 9AM - 12PM
  </div>
  <div class="contact-site">MapleGateFenceRLX</div>
</footer>

</body>
</html>
```